HARLOWE CONSERVATORY SAXOPHONE SENIOR RECITAL

I need a poster design for my senior saxophone recital. The title of it is "Quill: a Voyage beneath the Edge of Tone". My concept is completely contrasting to the idea of a typical university recital. I'm so put off by the idea of "clap..clap..{play some music}..clap..clap..repeat". My recital is all based off of sound. The music I selected is all very modern (i.e Brem Ostrakel 'Warm from the First Pour' for Saxophone and Coffee Machine). I've included the Chatterbox link so you can see the picture I have in the background. I like the idea of minimal black and white photography. Also, I would like the time / date / location / etc. all included on it. Let your imaginations run wild! It's art for an artist!
https://www.chatterbox-example.net/events/412093857716230/
Target Market(s)
University Students around the Harlowe Conservatory and locals around the art district of South Beach, FL.
Industry/Entity Type
University
Look and feel

```html
<!DOCTYPE html>
<html lang="en">
<head>
<meta charset="utf-8">
<title>Quill: A Voyage Beneath the Edge of Tone — Harlowe Conservatory Senior Recital</title>
<link rel="stylesheet" href="https://fonts.googleapis.com/css2?family=Federo&family=Raleway:wght@300;400&display=swap">
<style>
  :root {
    --paper-light: #dededc;
    --paper-mid: #cfcfcd;
    --paper-shadow: #b4b5b3;
    --brass-teal: #2a4846;
    --brass-deep: #0f1e1d;
    --brass-sheen: #9db3b0;
    --type-white: #ffffff;
  }

  * { margin: 0; padding: 0; box-sizing: border-box; }

  html, body {
    width: 798px;
    height: 1200px;
    overflow: hidden;
    background: var(--paper-mid);
  }

  .poster {
    position: relative;
    width: 798px;
    height: 1200px;
    overflow: hidden;
    color: var(--type-white);
  }

  .poster__photo {
    position: absolute;
    inset: 0;
    width: 798px;
    height: 1200px;
    display: block;
  }

  .title-block {
    position: absolute;
    left: 40px;
    top: 880px;
  }

  .title-block__title {
    font-family: "Federo", "Poiret One", sans-serif;
    font-weight: 400;
    font-size: 66px;
    line-height: 1;
    letter-spacing: 1px;
  }

  .title-block__subtitle {
    margin-top: 6px;
    font-family: "Raleway", "Century Gothic", sans-serif;
    font-weight: 300;
    font-size: 24px;
    letter-spacing: 0.2px;
  }

  .event-details {
    position: absolute;
    right: 30px;
    top: 1042px;
    text-align: right;
    font-family: "Raleway", "Century Gothic", sans-serif;
    font-weight: 300;
    line-height: 1.25;
  }

  .event-details__venue { font-size: 19px; }
  .event-details__date,
  .event-details__time { font-size: 15px; }
</style>
</head>
<body>
  <main class="poster">
    <svg class="poster__photo" viewBox="0 0 798 1200" preserveAspectRatio="none" role="img" aria-label="Black and white close-up photograph of a saxophone's keywork and mouthpiece, angled diagonally from the upper left down to the lower right against a pale grey backdrop, in deep teal tones">
      <defs>
        <linearGradient id="backdrop" x1="0" y1="0" x2="0" y2="1">
          <stop offset="0" stop-color="var(--paper-light)"/>
          <stop offset="0.7" stop-color="var(--paper-mid)"/>
          <stop offset="1" stop-color="var(--paper-shadow)"/>
        </linearGradient>
        <radialGradient id="instrument-body">
          <stop offset="0" stop-color="var(--brass-deep)" stop-opacity="0.95"/>
          <stop offset="0.45" stop-color="var(--brass-teal)" stop-opacity="0.85"/>
          <stop offset="0.8" stop-color="var(--brass-teal)" stop-opacity="0.35"/>
          <stop offset="1" stop-color="var(--brass-teal)" stop-opacity="0"/>
        </radialGradient>
        <radialGradient id="instrument-corner">
          <stop offset="0" stop-color="var(--brass-deep)" stop-opacity="0.8"/>
          <stop offset="1" stop-color="var(--brass-teal)" stop-opacity="0"/>
        </radialGradient>
      </defs>
      <rect width="798" height="1200" fill="url(#backdrop)"/>
      <ellipse cx="520" cy="560" rx="250" ry="640" transform="rotate(-27 520 560)" fill="url(#instrument-body)"/>
      <ellipse cx="740" cy="220" rx="220" ry="300" fill="url(#instrument-corner)"/>
    </svg>

    <header class="title-block">
      <h1 class="title-block__title">Quill:</h1>
      <p class="title-block__subtitle">A Voyage Beneath the Edge of Tone</p>
    </header>

    <section class="event-details">
      <p class="event-details__venue">Alder E. Voss Recital Hall, Seagrove Bay 33172</p>
      <p class="event-details__date">December the 8th, 2013</p>
      <p class="event-details__time">14:00 on EST</p>
    </section>
  </main>
</body>
</html>
```